Flyer Design Project for Brightwater Wellbeing Rooms

We are a psychology clinic that specialises in eating, parenting and chronic illness & pain. See our website for a summary.

We need a flyer that will go to doctors and schools in the local area.

Things to include on the front page:

Immediate appointments available
After hours appointments available
Male and female psychologists

Phone 9563 2190
Web brightwaterwellbeingrooms.com.au

On the back page:

Phone 9563 2190
Suite 1/1287 Marlowe Rd, Kelverton East 3185.
brightwaterwellbeingrooms.com.au

Parenting: Parenthood is an amazing journey, but for lots of people it raises all sorts of issues from fear of birth, breastfeeding difficulties and settling problems, to toddler discipline and food fussiness all the way through to getting help for your depressed or anxious adolescent. Our Parenting Psychologists can help you be the best parent you can be which will in turn lead to happier families, homes, children and parents.

Chronic illness/pain: Diabetes, heart disease, arthritis, asthma, migraines, dizziness, chronic fatigue syndrome, infertility, and PCOS are just some of the conditions that can be managed with psychological interventions. Everything we do is about helping you to manage your condition and get back to focusing on what you really want your life to be about.

Eating: Whether you suffer from anorexia, bulimia or binge eating, our strategies help you develop a healthy relationship with food and your body. The practical tips and strategies that we can provide are very useful for people undergoing lapband surgery or liposuction.

I am interested in whether the photographs that I have already purchased can be used...so please have a look through the website and see which you think will suit your design. Photographs are not absolutely necessary though, so if it doesn't fit with your idea that is okay too.
Updates

HI Everyone,

Thanks for submitting so far! I haven't found anything yet that has hit the mark. And I am thinking that is my fault and maybe that way i have described what I want. I apologise and hope that this update might help.

This brochure is likely to sit with lots of other brochures in a doctors waiting room so it needs to be different - so that it will be noticed.

The majority of our market are women - so something feminine is important. Maybe it needs to be a little more playful that I had initially thought. Like maybe not your standard blocky text and bolds and primary colours. But something more creative, more personal.

I want to not focus just on the family theme. Parenting is one area that we cover, but also we help people with eating disorders and chronic illness/chronic pain. So the photographs that I use need to be more general. It is importnat to focus on happy and healthy looking people. As we went to appeal to what my potential clients want to look like and feel like.

I do hope this helps to guide you. I promise that once I see a flyer that I could choose, I will turn the funding to guaranteed. I did this last time...I am just a bit nervous as I haven't received anything yet that I am excited about.

Kindest regards,

Marnie.

Hi Everyone,

Thank you for your designs coming in! As promised, as soon as I received a design that I could see myself choosing I would change the status from refundable to committed. I have now done this!

I have received a design that I would say is good. It is not perfect however...so please keep the ideas coming.

To give more direction, the one that came in has a nice theme that runs through the brochure. Not too many different types of font and colours detracting from the flow of the flyer. However, the thing that I am concerned about is whether it will stand out enough on a rack of other flyers in a doctors waiting room.

I hope this helps with your creative ideas.

Thanks again to everyone!

Marnie.

Thanks SO much to everyone who is putting in designs. You are making my decision difficult!

I am wondering if you can update your designs with a few things:

can I ask you to make some text changes:

1. Can we have a heading on the front page: Psychologists  and then can you put Kelverton East in smaller writing just below it?

2. Id like to say on the front: Specialising in parenting, disordered eating and chronic pain & illness

3. Delete Male & Female Psychologists

4. In general we dont' need to have the logo standing out. We don't have a well known brand yet, so I am not wanting to take up valuable space with this - so perhaps it shoudl be small and maybe just on the back? Keeping the name of our clinic on the front with the website shoudl be sufficient.

Thanks heaps everyone...I will make decision very soon!

Target Market(s)

20-40 year olds. Working. Educated. Female. They might have a family/children.
Australian. Engish speaking.

Industry/Entity Type

Clinic

Requirements
Must have
• I would like to include our logo. Please do not use the colour green that it is in. I hate that colour! but I LOVE the logo.

I would like to follow through with some of the themes of the website and other stationary.

I will attach some of the other stationary I have had designed.

I really like the colours in the letterhead - especially that blue of the logo.

I think it needs to have a dash of colour with it at least...something that will stand out and be noticed on a brochure rack...but also have a look of class/sophistication/modern.
Nice to have
• Perhaps photograph of happy and healthy people.
Should not have
• I don't like bold text or too many different types of fonts.

It shouldn't look too cluttered so I might need to reduce the text I have included - I will need to see it first.

```html
<!DOCTYPE html>
<html lang="en">
<head>
<meta charset="utf-8">
<title>Brightwater Wellbeing Rooms – Flyer</title>
<link rel="stylesheet" href="https://fonts.googleapis.com/css2?family=Source+Sans+3:wght@400;600&display=swap">
<style>
:root{
  --bg:#979797;
  --paper:#ffffff;
  --teal-dark:#1f6a70;
  --teal-light:#62c3c9;
  --yellow:#f1e81f;
  --ink:#2f2f2f;
  --strip-1:#6aa38a;
  --strip-2:#86c9cb;
  --strip-3:#5f9da2;
  --strip-4:#3f7b7d;
  --strip-5:#a7d8d6;
}
*{margin:0;padding:0;box-sizing:border-box}
html,body{width:1200px;height:1109px;overflow:hidden}
body{background:var(--bg);font-family:"Source Sans 3",Arial,sans-serif;color:var(--ink);position:relative}

.panel{position:absolute;top:0;height:1109px;background:var(--paper);overflow:hidden}
.panel--front{left:63px;width:520px}
.panel--back{left:627px;width:515px}

.colour-strip{position:absolute;left:0;width:100%;height:22px;display:flex}
.colour-strip span{flex:1}
.colour-strip span:nth-child(5n+1){background:var(--strip-1)}
.colour-strip span:nth-child(5n+2){background:var(--strip-2)}
.colour-strip span:nth-child(5n+3){background:var(--strip-3)}
.colour-strip span:nth-child(5n+4){background:var(--strip-4)}
.colour-strip span:nth-child(5n+5){background:var(--strip-5)}
.colour-strip--top{top:0}
.colour-strip--bottom{bottom:0;height:25px}

/* front */
.headline{position:absolute;top:69px;left:0;width:100%;height:94px;background:var(--teal-dark);
  color:#fff;font-size:49px;font-weight:400;line-height:94px;text-align:center;letter-spacing:-.3px}
.headline b{color:var(--yellow);font-weight:400}

.hero-photo{position:absolute;top:205px;left:0;width:100%;height:335px;
  background:linear-gradient(120deg,#b98e6c 0%,#d9b59a 35%,#8a6b52 60%,#c79b86 100%)}
.focus-areas{position:absolute;top:212px;left:227px;width:340px;height:322px;border-radius:50%;
  background:var(--yellow);padding:38px 67px 0 0;text-align:right;color:#3a3a3a;font-size:38px;line-height:1.1}
.focus-areas p{margin-bottom:18px}
.focus-areas p.multi{line-height:1.05}

.services{position:absolute;top:570px;left:18px;list-style:none}
.services li{display:flex;align-items:center;height:65px;font-size:29px;letter-spacing:.3px;color:#333}
.services svg{margin-right:14px}

.cta{position:absolute;left:0;width:100%;display:flex}
.cta__label{position:relative;z-index:1;background:var(--teal-dark);color:#fff;text-align:center;
  clip-path:polygon(0 0,85% 0,100% 50%,85% 100%,0 100%)}
.cta__band{flex:1;background:var(--teal-light);color:#fff;margin-left:-30px}
.cta--front{top:783px;height:109px}
.cta--front .cta__label{width:212px;font-size:23px;line-height:1.2;padding:14px 30px 0 6px}
.cta--front .cta__band{font-size:40px;line-height:109px;padding-left:52px}

.clinic-name{position:absolute;top:936px;left:0;width:100%;display:flex;justify-content:center;align-items:center;
  color:var(--teal-light);font-size:22px;letter-spacing:1px;text-transform:uppercase}
.clinic-name i{width:22px;height:22px;border:3px solid var(--teal-light);border-radius:50%;margin-right:12px}

.web-bar{position:absolute;top:1019px;left:0;width:100%;height:50px;background:var(--yellow);
  text-align:center;line-height:50px;font-size:22px;color:#333}

/* back */
.topic-heading{position:absolute;left:0;width:100%;height:42px;background:var(--teal-light);color:#fff;
  font-size:29px;line-height:42px;padding-left:22px;letter-spacing:.5px;font-weight:400}
.topic-text{position:absolute;left:22px;width:470px;font-size:18.4px;line-height:31.5px;color:#2c2c2c}
.h-parenting{top:15px}.t-parenting{top:70px}
.h-chronic{top:344px}.t-chronic{top:398px}
.h-eating{top:640px}.t-eating{top:700px}

.cta--back{top:879px;height:127px}
.cta--back .cta__label{width:165px;font-size:32px;line-height:1.05;padding:12px 32px 0 0}
.cta--back .cta__band{text-align:center;padding:18px 0 0 20px}
.cta--back .call{font-size:41px;line-height:1.05}
.cta--back .visit{font-size:19px}

.address{position:absolute;top:1040px;left:0;width:100%;text-align:center;font-size:19px;color:#333}
</style>
</head>
<body>

<section class="panel panel--front">
  <div class="colour-strip colour-strip--top"><span></span><span></span><span></span><span></span><span></span><span></span><span></span></div>

  <h1 class="headline"><b>E</b>xpert <b>F</b>amily <b>A</b>dvice</h1>

  <div class="hero-photo" role="img" aria-label="Photograph of a smiling mother with her toddler outdoors"></div>
  <div class="focus-areas">
    <p>Parenting</p>
    <p>Eating</p>
    <p class="multi">Chronic Pain<br>&amp; Illness</p>
  </div>

  <ul class="services">
    <li><svg width="26" height="26" viewBox="0 0 26 26"><circle cx="13" cy="13" r="10" fill="none" stroke="#1f6a70" stroke-width="3"/></svg>IMMEDIATE APPOINTMENTS</li>
    <li><svg width="26" height="26" viewBox="0 0 26 26"><circle cx="13" cy="13" r="10" fill="none" stroke="#1f6a70" stroke-width="3"/></svg>AFTERHOURS APPOINTMENTS</li>
    <li><svg width="26" height="26" viewBox="0 0 26 26"><circle cx="13" cy="13" r="10" fill="none" stroke="#1f6a70" stroke-width="3"/></svg>MALE &amp; FEMALE PSYCHOLOGISTS</li>
  </ul>

  <div class="cta cta--front">
    <div class="cta__label">Make your appointment today!</div>
    <div class="cta__band">Call: 9563 2190</div>
  </div>

  <div class="clinic-name"><i></i>Brightwater Wellbeing Rooms</div>

  <div class="web-bar">brightwaterwellbeingrooms.com.au</div>

  <div class="colour-strip colour-strip--bottom"><span></span><span></span><span></span><span></span><span></span><span></span><span></span></div>
</section>

<section class="panel panel--back">
  <h2 class="topic-heading h-parenting">PARENTING</h2>
  <p class="topic-text t-parenting">Parenthood is an amazing journey, but for lots of people it raises all sorts of issues from fear of birth, breastfeeding difficulties and settling problems, to toddler discipline and food fussiness all the way through to getting help for your depressed or anxious adolescent. Our Parenting Psychologists can help you be the best parent you can be which will in turn lead to happier families, homes, children and parents.</p>

  <h2 class="topic-heading h-chronic">CHRONIC PAIN &amp; ILLNESS</h2>
  <p class="topic-text t-chronic">Diabetes, heart disease, arthritis, asthma, migraines, dizziness, chronic fatigue syndrome, infertility, and PCOS are just some of the conditions that can be managed with psychological interventions. Everything we do is about helping you to manage your condition and get back to focusing on what you really want your life to be about.</p>

  <h2 class="topic-heading h-eating">EATING</h2>
  <p class="topic-text t-eating">Whether you suffer from anorexia, bulimia or binge eating, our strategies help you develop a healthy relationship with food and your body. The practical tips and strategies that we can provide are very useful for people undergoing lapband surgery or liposuction.</p>

  <div class="cta cta--back">
    <div class="cta__label">For<br>more<br>info:</div>
    <div class="cta__band">
      <div class="call">Call: 9563 2190</div>
      <div class="visit">Or visit: brightwaterwellbeingrooms.com.au</div>
    </div>
  </div>

  <p class="address">Suite 1/1287 Marlowe Rd. Kelverton East 3185</p>

  <div class="colour-strip colour-strip--bottom"><span></span><span></span><span></span><span></span><span></span><span></span><span></span></div>
</section>

</body>
</html>
```